依頼詳細
■商品の特徴
・使用する原材料は「小麦粉・塩・水」のみ。厳選した国産小麦粉をたっぷりの水で捏ね、みずみずしい透明感とツヤのある麺に仕上げました。
・麺の太さは、細すぎず、適度な噛みごたえ、食べ応えが楽しめます。
・油を使っていないシンプルな原材料で安心感も併せて訴求。

■デザインの方向性
・和紙(雲竜またはカルミナ)の風合いを生かす
・和モダン、シンプル、品がある、
・素朴で田舎っぽいがお洒落なイメージも想起させる。
・夏、涼しい、冷たい、水、流れ、波紋など、涼感を想起させるイメージ。
・商品名が筆文字の場合は、達筆すぎない、崩れすぎていない、読みやすいこと。

■留意点
・ジジ臭いのはNG(蕎麦やうどんは、とかくジジ臭くなりがちです)

■ 利用用途
・決定したデザインはそうめんの他、冷麦などシリーズ展開します。
記載項目
■パッケージ仕様
・商品名:青峰の細打ち冷や糸(仮名)
・フィルム寸法:W230×H275(オモテ面 W100×H275の範囲をデザイン)
・フィルム材質:レーヨン紙(雲竜またはカルミナ)
・色数:5色まで(シズルは無し)
希望イメージ
シンプル 複雑
単色 カラフル
暗い 明るい
日常 高級
遊び心 厳粛
未来的 伝統的
女性的 男性的
希望する色
青系、水色系、グレー系、紫系
納品ファイル
• 高解像度JPG (.jpg)
• イラストレーター形式 (.ai)
• フォトショップ形式 (.psd)
補足説明
合成用の画像を用意しましたので、可能であればこの画像に合成してご提案いただけますでしょか?よろしくお願い致します。
■ 選んだ理由

和風、モダンさのバランスが求めていたものに近い気がしました。売り場のイメージにもマッチしていると感じました。色を変えてのシリーズ展開もしやすそうでした。白を生かした涼感も感じました。

■ 提案者全員のお礼・コメント

この度は素敵なデザインのご提案ありがとうございます。こちらのデザインを元に修正もお願いするかと思います。その際はよろしくお願いいたします。
まずは、修正の方向性を私の方で探って見たいので、イラレのデータをいただけますでしょうか?よろしくお願いいたします。

```html
<!DOCTYPE html>
<html lang="ja">
<head>
<meta charset="UTF-8">
<title>青峰の細打ち冷や糸 パッケージ</title>
<link rel="stylesheet" href="https://fonts.googleapis.com/css2?family=Yuji+Syuku&family=Shippori+Mincho+B1:wght@700&display=swap">
<style>
  :root {
    --page: #ffffff;
    --paper: #ffffff;
    --water: #d4e9f6;
    --water-soft: #e8f4fb;
    --ink: #2b2b2b;
    --violet: #6a3a8c;
    --badge-text: #ffffff;
    --shadow: rgba(0, 0, 0, 0.22);
  }
  html, body {
    margin: 0;
    padding: 0;
    width: 1200px;
    height: 2504px;
    overflow: hidden;
    background: var(--page);
  }
  .package-front {
    position: absolute;
    left: 140px;
    top: 88px;
    width: 932px;
    height: 2320px;
    background: var(--paper);
    box-shadow: 10px 12px 14px var(--shadow);
    overflow: hidden;
  }
  .water-flow {
    position: absolute;
    inset: 0;
    background:
      radial-gradient(ellipse 70% 22% at 70% 8%, var(--water) 0%, var(--water) 55%, transparent 75%),
      radial-gradient(ellipse 60% 18% at 15% 30%, var(--water-soft) 0%, transparent 70%),
      radial-gradient(ellipse 90% 30% at 40% 92%, var(--water) 0%, var(--water) 55%, transparent 78%),
      linear-gradient(180deg, var(--water) 0%, var(--water-soft) 22%, var(--paper) 38%, var(--paper) 58%, var(--water-soft) 70%, var(--water) 85%);
  }
  .name-badge {
    position: absolute;
    left: 572px;
    top: 232px;
    width: 128px;
    height: 720px;
  }
  .name-badge svg {
    position: absolute;
    inset: 0;
  }
  .badge-label {
    position: absolute;
    left: 0;
    top: 120px;
    width: 128px;
    writing-mode: vertical-rl;
    display: flex;
    align-items: center;
    font-family: "Shippori Mincho B1", serif;
    font-weight: 700;
    font-size: 84px;
    letter-spacing: 6px;
    line-height: 128px;
    color: var(--badge-text);
  }
  .product-name {
    position: absolute;
    left: 330px;
    top: 460px;
    width: 200px;
    margin: 0;
    writing-mode: vertical-rl;
    font-family: "Yuji Syuku", serif;
    font-weight: 400;
    font-size: 172px;
    line-height: 200px;
    letter-spacing: 10px;
    color: var(--ink);
  }
</style>
</head>
<body>
  <main class="package-front">
    <div class="water-flow" role="img" aria-label="白い水流と波紋が流れる淡い水色の涼しげな模様"></div>

    <div class="name-badge">
      <svg width="128" height="720" viewBox="0 0 128 720" aria-hidden="true">
        <polyline points="4,46 64,8 124,46" fill="none" stroke="var(--violet)" stroke-width="4"/>
        <polygon points="0,82 64,42 128,82 128,638 64,678 0,638" fill="var(--violet)"/>
        <polyline points="4,674 64,712 124,674" fill="none" stroke="var(--violet)" stroke-width="4"/>
      </svg>
      <div class="badge-label">青峰の</div>
    </div>

    <h1 class="product-name">細打ち冷や糸</h1>
  </main>
</body>
</html>
```